Hollis Ironworks Business Card

We need a business card design for a new small metal fabrication business in rural NSW, Australia.

The business (Hollis Ironworks) is owner operated by a man with the initials RB - much of the branding comes from this name.

Hollis Ironworks designs, engineers, repairs and manufactures a range of custom, quality metal works including vehicle trays, agricultural machinery impliments, trailers, wood splitters, fire pits, furniture etc.

The brand position focuses on custom work of the highest quality.

Business card design should show quality, attention to detail and stand out among a mass of business cards.

Logos are in the files

The grey color may be changed on the logo if required to stand out more.

There is an image attached of a simple card that is liked because it is clean, clear, simple, masculine and effective. It says 'quality'. As most of the work we do is custom it would be good to have the business card speak to this.

Target Market(s)

Rural and regional based Australians. Primarily adult male 25-60 yrs. Primary production / rural / travelling lifestyle.

Industry/Entity Type

Metal Fabrication

Contact Information for Business Card

The words 'custom quality fabrications' would be great somewhere perhaps on the backside (not on the information side)
Name
title
Phone: 0491 538 274 and (02) 7342 9185
email: info@hollisiw.com.au
www.hollisiw.com.au

address (2 lines)

Requirements
Nice to have
• Background colour should be very navy blue or black.
Should not have
• NO orange and blue combinations.
• Navy is OK

```html
<!DOCTYPE html>
<html lang="en">
<head>
<meta charset="utf-8">
<title>Hollis Ironworks Business Card</title>
<link rel="stylesheet" href="https://fonts.googleapis.com/css2?family=Source+Sans+3:wght@400;600;700&display=swap">
<style>
  :root {
    --backdrop: #e6e4e1;
    --card-light: #ffffff;
    --card-dark: #1d1d1d;
    --ink: #1e1e1e;
    --steel: #a9a9a9;
    --weld-green: #6cc04a;
  }
  * { margin: 0; padding: 0; box-sizing: border-box; }
  html, body {
    width: 1200px;
    height: 900px;
    overflow: hidden;
    background: var(--backdrop);
    font-family: "Source Sans 3", Arial, sans-serif;
  }
  .canvas {
    position: relative;
    width: 1200px;
    height: 900px;
  }
  .card {
    position: absolute;
    border-radius: 16px;
    box-shadow: 0 6px 18px rgba(0, 0, 0, 0.18);
  }
  .card--info {
    left: 78px;
    top: 35px;
    width: 587px;
    height: 363px;
    background: var(--card-light);
    color: var(--ink);
    text-align: center;
  }
  .person-name {
    position: absolute;
    top: 106px;
    left: 0;
    width: 100%;
    font-size: 23px;
    font-weight: 600;
    line-height: 1.1;
  }
  .person-title {
    position: absolute;
    top: 134px;
    left: 0;
    width: 100%;
    font-size: 15.5px;
    font-weight: 400;
  }
  .divider {
    position: absolute;
    top: 164px;
    left: 216px;
    width: 155px;
    height: 2px;
    background: var(--ink);
  }
  .contact-list {
    position: absolute;
    top: 183px;
    left: 0;
    width: 100%;
    list-style: none;
    font-size: 16px;
    line-height: 24.5px;
  }
  .address {
    position: absolute;
    top: 293px;
    left: 0;
    width: 100%;
    font-size: 16px;
  }
  .card--brand {
    left: 390px;
    top: 507px;
    width: 563px;
    height: 348px;
    background: var(--card-dark);
  }
  .brand-lockup {
    position: absolute;
    left: 68px;
    top: 134px;
    display: flex;
    align-items: center;
    gap: 18px;
  }
  .brand-mark {
    width: 64px;
    height: 64px;
    background: var(--weld-green);
  }
  .brand-name {
    color: var(--steel);
    font-size: 42px;
    font-weight: 700;
    letter-spacing: 2px;
    text-transform: uppercase;
    line-height: 1;
  }
</style>
</head>
<body>
  <main class="canvas">
    <section class="card card--info" aria-label="Business card contact side">
      <h1 class="person-name">Marcus Reid</h1>
      <p class="person-title">Managing Director</p>
      <div class="divider"></div>
      <ul class="contact-list">
        <li>0491 538 274</li>
        <li>(02) 7342 9185</li>
        <li>info@hollisiw.com.au</li>
        <li>www.hollisiw.com.au</li>
      </ul>
      <p class="address">12345, Address Goes Here Country Name, 123456</p>
    </section>

    <section class="card card--brand" aria-label="Business card brand side">
      <div class="brand-lockup">
        <div class="brand-mark"></div>
        <p class="brand-name">Hollis Ironworks</p>
      </div>
    </section>
  </main>
</body>
</html>
```